rl ironcraft business card metallic look

revamp the existing design but want card to have a metalic look to it

Target Market(s)

construction industry

Industry/Entity Type

constrction

Contact Information for Business Card

front of card RL Ironcraft, phone 4163920857, email rl.ironcraftt@quellmail.example and instagram account; rl_ironcraft_

Font styles to use
Other font styles liked:
• masculine

Colors

Designer to choose only greyscale colors for use in the design.

Requirements
Must have
• back side RL Ironcraft then a list of everything : Siding, ACM Panels, Standing Seam,Soffit, Fascia, Gutters,Metal,Alu,inum, Viynyl, Metal Roofs and roof repairs
Nice to have
• I would like to keep the look of the existing card with the metal grids on the front
Should not have
• Need a design in two days

```html
<!DOCTYPE html>
<html lang="en">
<head>
<meta charset="utf-8">
<title>RL Ironcraft – Business Card</title>
<link href="https://fonts.googleapis.com/css2?family=Oswald:wght@600;700&family=Cabin+Condensed:wght@700&display=swap" rel="stylesheet">
<style>
  :root{
    --page:#ffffff;
    --front-bg:#5f5f61;
    --back-bg:#d1d2d4;
    --edge:#3a3a3a;
    --silver:#e4e4e6;
    --ink-dark:#3c3c3e;
    --stripe-light:#cfcfd1;
    --outline:#2e2e30;
  }
  *{margin:0;padding:0;box-sizing:border-box}
  html,body{width:1005px;height:1200px;overflow:hidden;background:var(--page)}
  .sheet{position:relative;width:1005px;height:1200px}
  .card{position:absolute;left:1px;width:1002px;height:570px;border:1px solid var(--edge);overflow:hidden}
  .card--front{top:1px;background:var(--front-bg)}
  .card--back{top:628px;height:550px;background:var(--back-bg)}
  .card__bands{position:absolute;inset:0;width:100%;height:100%}
  .brand{position:absolute;left:0;right:0;text-align:center;font-family:'Oswald',sans-serif;font-weight:700;text-transform:uppercase;letter-spacing:6px;line-height:1}
  .card--front .brand{top:120px;font-size:104px;color:var(--silver)}
  .card--back .brand{top:70px;font-size:100px;color:var(--ink-dark)}
  .contact{position:absolute;left:299px;top:330px;list-style:none}
  .contact__item{display:flex;align-items:center;color:var(--silver);font-family:'Cabin Condensed',sans-serif;font-weight:700}
  .contact__icon{width:40px;flex:0 0 40px;margin-right:20px;display:flex;justify-content:center}
  .contact__item--phone{height:44px;font-family:'Oswald',sans-serif;font-weight:600;font-size:34px;letter-spacing:5px}
  .contact__item--mail{height:40px;margin-top:6px;font-size:22px;letter-spacing:.3px}
  .contact__item--social{height:40px;margin-top:10px;font-size:22px}
  .contact__item span{-webkit-text-stroke:0.6px var(--outline);paint-order:stroke fill}
  .services{position:absolute;left:60px;right:60px;top:286px;text-align:center;font-family:'Cabin Condensed',sans-serif;font-weight:700;font-size:41px;line-height:53px;color:#fff;-webkit-text-stroke:5px var(--outline);paint-order:stroke fill}
</style>
</head>
<body>
<main class="sheet">

  <section class="card card--front" aria-label="Card front">
    <svg class="card__bands" viewBox="0 0 1002 570" aria-hidden="true">
      <defs>
        <linearGradient id="bandL" x1="0" y1="0" x2="1" y2="1">
          <stop offset="0" stop-color="#9a9a9c"/><stop offset=".5" stop-color="#dcdcde"/><stop offset="1" stop-color="#8a8a8c"/>
        </linearGradient>
        <linearGradient id="bandR" x1="1" y1="0" x2="0" y2="1">
          <stop offset="0" stop-color="#9a9a9c"/><stop offset=".5" stop-color="#dcdcde"/><stop offset="1" stop-color="#8a8a8c"/>
        </linearGradient>
        <linearGradient id="corrugated" x1="0" y1="0" x2="1" y2="0">
          <stop offset="0" stop-color="#2a2a2b"/><stop offset=".5" stop-color="#4a4a4c"/><stop offset="1" stop-color="#2e2e30"/>
        </linearGradient>
      </defs>
      <polygon points="0,140 150,0 166,0 0,156" fill="url(#bandL)" opacity=".55"/>
      <polygon points="0,300 175,437 150,437 0,328" fill="url(#bandL)"/>
      <polygon points="0,357 258,570 226,570 0,392" fill="url(#bandL)"/>
      <polygon points="1002,300 827,437 852,437 1002,328" fill="url(#bandR)"/>
      <polygon points="1002,357 744,570 776,570 1002,392" fill="url(#bandR)"/>
      <polygon role="img" aria-label="Corrugated metal sheet texture" points="657,47 718,0 1002,0 1002,200 970,226" fill="url(#corrugated)"/>
    </svg>

    <h1 class="brand">RL Ironcraft</h1>

    <ul class="contact">
      <li class="contact__item contact__item--phone">
        <span class="contact__icon">
          <svg width="38" height="38" viewBox="0 0 24 24" aria-hidden="true"><path d="M6.6 10.8a15.1 15.1 0 0 0 6.6 6.6l2.2-2.2a1 1 0 0 1 1-.25 11.4 11.4 0 0 0 3.6.57 1 1 0 0 1 1 1V20a1 1 0 0 1-1 1A17 17 0 0 1 3 4a1 1 0 0 1 1-1h3.5a1 1 0 0 1 1 1c0 1.25.2 2.45.57 3.57a1 1 0 0 1-.25 1z" fill="none" stroke="#fff" stroke-width="1.6"/></svg>
        </span>
        <span>416-392-0857</span>
      </li>
      <li class="contact__item contact__item--mail">
        <span class="contact__icon">
          <svg width="36" height="28" viewBox="0 0 36 28" aria-hidden="true"><rect x="1" y="1" width="34" height="26" fill="#fff" stroke="#2e2e30" stroke-width="1.5"/><path d="M1 1l17 14L35 1M1 27l12-13M35 27L23 14" fill="none" stroke="#2e2e30" stroke-width="1.2"/></svg>
        </span>
        <span>rl.ironcraftt@quellmail.example</span>
      </li>
      <li class="contact__item contact__item--social">
        <span class="contact__icon">
          <svg width="36" height="36" viewBox="0 0 36 36" aria-hidden="true"><rect x="2" y="2" width="32" height="32" rx="7" fill="none" stroke="#fff" stroke-width="3"/></svg>
        </span>
        <span>rl_ironcraft_</span>
      </li>
    </ul>
  </section>

  <section class="card card--back" aria-label="Card back">
    <svg class="card__bands" viewBox="0 0 1002 550" aria-hidden="true">
      <defs>
        <linearGradient id="bandLb" x1="0" y1="0" x2="1" y2="1">
          <stop offset="0" stop-color="#b8b8ba"/><stop offset=".5" stop-color="#f0f0f1"/><stop offset="1" stop-color="#a6a6a8"/>
        </linearGradient>
        <linearGradient id="bandRb" x1="1" y1="0" x2="0" y2="1">
          <stop offset="0" stop-color="#b8b8ba"/><stop offset=".5" stop-color="#f0f0f1"/><stop offset="1" stop-color="#a6a6a8"/>
        </linearGradient>
      </defs>
      <polygon points="0,293 175,430 150,430 0,320" fill="url(#bandLb)"/>
      <polygon points="0,345 258,550 226,550 0,380" fill="url(#bandLb)"/>
      <polygon points="1002,293 827,430 852,430 1002,320" fill="url(#bandRb)"/>
      <polygon points="1002,345 744,550 776,550 1002,380" fill="url(#bandRb)"/>
    </svg>

    <h2 class="brand">RL Ironcraft</h2>

    <p class="services">Siding, ACM Panels, Standing Seam,<br>Soffit, Fascia, Gutters, Metal,<br>Aluminum, Vynyl, Metal Roof And<br>Roffing Repairs</p>
  </section>

</main>
</body>
</html>
```